Letterhead to Prospective Clients

Create a letterhead (word & canva) that I will use to send letters to prospective clients and also include the Coralwood Estate Partners Logo, My Contact Details and Interchangeable "Suburb". Use the same font and colour pallete

Maris Dulworth | "Suburb" Specialist - Redlands & Surrounds
Mobile: 0417 862 095
Email: MD@CoralwoodEstatePartners.com.au

```html
<!DOCTYPE html>
<html lang="en">
<head>
<meta charset="UTF-8">
<title>Coralwood Estate Partners – Letterhead</title>
<link href="https://fonts.googleapis.com/css2?family=Poppins:wght@300;400;500;600&display=swap" rel="stylesheet">
<style>
  :root {
    --backdrop: #cccccc;
    --paper: #ffffff;
    --navy: #132a42;
    --sand: #d6ab7d;
  }
  * { margin: 0; padding: 0; box-sizing: border-box; }
  html, body {
    width: 1200px; height: 1200px; overflow: hidden;
    background: var(--backdrop);
    font-family: "Poppins", sans-serif;
    color: var(--navy);
  }
  .letterhead {
    position: absolute; left: 221px; top: 110px;
    width: 758px; height: 980px;
    background: var(--paper);
    overflow: hidden;
  }
  .brand-name {
    position: absolute; left: 0; top: 76px; width: 100%;
    text-align: center; font-weight: 300;
    font-size: 64px; line-height: 1;
    letter-spacing: 0.05em; padding-left: 0.05em;
    color: var(--navy);
  }
  .brand-sub {
    position: absolute; left: 0; top: 161px; width: 100%;
    text-align: center; font-weight: 400;
    font-size: 13px; line-height: 1;
    letter-spacing: 0.42em; padding-left: 0.42em;
    color: var(--sand);
  }
  .headline {
    position: absolute; left: 84px; top: 265px;
    font-size: 45px; font-weight: 600; letter-spacing: -0.01em; line-height: 1;
  }
  .body-copy {
    position: absolute; left: 86px; top: 335px; width: 620px;
    font-size: 13.2px; line-height: 23px; font-weight: 400; letter-spacing: -0.005em;
  }
  .body-copy p + p { margin-top: 23px; }
  .contact-list {
    position: absolute; left: 86px; top: 656px; list-style: none;
    font-size: 14.1px; line-height: 22px;
  }
  .contact-list li { display: flex; align-items: center; height: 22px; }
  .contact-list svg { width: 13px; height: 13px; margin-right: 13px; fill: var(--navy); flex: none; }
  .signature {
    position: absolute; left: 84px; top: 802px;
    font-size: 23.6px; line-height: 26px; font-weight: 400;
  }
</style>
</head>
<body>
  <main class="letterhead">
    <header class="brand">
      <span class="brand-name">CORALWOOD</span>
      <span class="brand-sub">ESTATE PARTNERS</span>
    </header>

    <h1 class="headline">HEADLINE</h1>

    <section class="body-copy">
      <p>Lorem ipsum dolor sit amet consectetur adipiscing elit. Quisque faucibus ex sapien vitae<br>pellentesque sem placerat. In id cursus mi pretium tellus duis convallis. Tempus leo<br>eu aenean sed diam urna tempor. Pulvinar vivamus fringilla lacus nec metus bibendum<br>egestas. Iaculis massa nisl malesuada lacinia integer nunc posuere. Ut hendrerit semper<br>vel class aptent taciti sociosqu. Ad litora torquent per conubia nostra inceptos himenaeos.</p>
      <p>Lorem ipsum dolor sit amet consectetur adipiscing elit. Quisque faucibus ex sapien vitae<br>pellentesque sem placerat. In id cursus mi pretium tellus duis convallis. Tempus leo eu<br>aenean sed diam urna tempor. Pulvinar vivamus fringilla lacus nec metus bibendum<br>egestas. Iaculis massa nisl malesuada lacinia integer nunc posuere. Ut hendrerit semper<br>vel class aptent taciti sociosqu. Ad litora torquent per conubia nostra Inceptos himenaeos.</p>
    </section>

    <ul class="contact-list">
      <li>
        <svg viewBox="0 0 24 24" aria-hidden="true"><path d="M12 1a8 8 0 0 0-8 8c0 6 8 14 8 14s8-8 8-14a8 8 0 0 0-8-8zm0 11a3 3 0 1 1 0-6 3 3 0 0 1 0 6z"/></svg>
        123 Dummy, Lorem Ipsum
      </li>
      <li>
        <svg viewBox="0 0 24 24" aria-hidden="true"><path d="M6.6 10.8a15 15 0 0 0 6.6 6.6l2.2-2.2c.3-.3.7-.4 1-.2 1.1.4 2.300.6 3.6.6.6 0 1 .4 1 1V20c0 .6-.4 1-1 1A17 17 0 0 1 3 4c0-.6.4-1 1-1h3.5c.6 0 1 .4 1 1 0 1.3.2 2.5.6 3.6.1.3 0 .7-.2 1z"/></svg>
        0417 862 095
      </li>
      <li>
        <svg viewBox="0 0 24 24" aria-hidden="true"><path d="M1 5h22v14H1zM2.5 6.5v.4L12 13l9.5-6.1v-.4zM2.5 8.7v8.8l6-4.9zm19 0-6 3.9 6 4.9zM9.8 13.4l-6.7 4.1h17.8l-6.7-4.1L12 14.8z"/></svg>
        info@email space
      </li>
      <li>
        <svg viewBox="0 0 24 24" aria-hidden="true"><path d="M12 1a11 11 0 1 0 0 22 11 11 0 0 0 0-22zm-1 2.2V7H8a9 9 0 0 1 3-3.8zm2 0A9 9 0 0 1 16 7h-3zM4 9h3.4a16 16 0 0 0-.2 2H3.1A9 9 0 0 1 4 9zm5.5 0H11v2H9.3c0-.7.1-1.4.2-2zM13 9h1.5c.1.6.2 1.3.2 2H13zm3.6 0H20a9 9 0 0 1 .9 2h-4.1a16 16 0 0 0-.2-2zM3.1 13h4.1c0 .7.1 1.4.2 2H4a9 9 0 0 1-.9-2zm6.2 0H11v2H9.5c-.1-.6-.2-1.3-.2-2zm3.7 0h1.7c0 .7-.1 1.4-.2 2H13zm3.8 0h4.1a9 9 0 0 1-.9 2h-3.4c.1-.6.2-1.3.2-2zM8 17h3v3.8A9 9 0 0 1 8 17zm5 0h3a9 9 0 0 1-3 3.8z"/></svg>
        MD@CoralwoodEstatePartners.com.au
      </li>
    </ul>

    <footer class="signature">
      <p>Maris Dulworth</p>
      <p>“Suburb” Specialist</p>
      <p>Redlands &amp; Surrounds</p>
    </footer>
  </main>
</body>
</html>
```